TalkBridge - Language Coaching Services

Sleek, innovative, trendy design for Language Coaching business.

TalkBridge is a new UK based company that provides Language Coaching services. We offer highly personalized on-line and face to face language courses. We also impart learning techniques workshops based on the latest neuroscience research for second-language acquisition.

Target Market(s)

Industry/Entity Type

Consulting

Contact Information for Business Card

TalkBridge
ElenaVT@talkbridge-demo.co.uk
TalkBridge-demo.co.uk
London, UK

Font styles to use
Sans Serif

```html
<!DOCTYPE html>
<html lang="en">
<head>
<meta charset="utf-8">
<title>TalkBridge – Business Card</title>
<link rel="stylesheet" href="https://fonts.googleapis.com/css2?family=Montserrat:wght@600&family=Questrial&display=swap">
<style>
  :root {
    --backdrop: #ececec;
    --card: #ffffff;
    --ink: #0f5a85;
    --brand: #0a8cc0;
  }
  * { margin: 0; padding: 0; box-sizing: border-box; }
  html, body {
    width: 1180px;
    height: 1200px;
    overflow: hidden;
    background: var(--backdrop);
  }
  .canvas {
    position: relative;
    width: 1180px;
    height: 1200px;
  }
  .card {
    position: absolute;
    left: 225px;
    width: 729px;
    height: 473px;
    background: var(--card);
  }
  .card--front { top: 100px; }
  .card--back  { top: 627px; }

  .brand-mark {
    position: absolute;
    left: 50%;
    top: 150px;
    width: 126px;
    height: 126px;
    margin-left: -63px;
  }
  .brand-name {
    position: absolute;
    left: 0;
    right: 0;
    top: 280px;
    text-align: center;
    font-family: "Questrial", sans-serif;
    font-size: 52px;
    line-height: 1;
    color: var(--brand);
    letter-spacing: 0.01em;
  }

  .contact {
    position: absolute;
    left: 0;
    right: 0;
    top: 150px;
    text-align: center;
    color: var(--ink);
  }
  .contact__title {
    font-family: "Montserrat", sans-serif;
    font-weight: 600;
    font-size: 25px;
    letter-spacing: 0.5em;
    margin-right: -0.5em;
    line-height: 30px;
  }
  .contact__dot {
    display: block;
    width: 12px;
    height: 12px;
    border-radius: 50%;
    background: var(--ink);
    margin: 17px auto 20px;
  }
  .contact__line {
    font-family: "Questrial", sans-serif;
    font-size: 22px;
    letter-spacing: 0.08em;
    line-height: 36.5px;
  }
</style>
</head>
<body>
  <main class="canvas">
    <section class="card card--front" aria-label="Business card front">
      <svg class="brand-mark" viewBox="0 0 126 126" aria-hidden="true">
        <circle cx="63" cy="63" r="60" fill="none" stroke="var(--brand)" stroke-width="5"/>
      </svg>
      <p class="brand-name">TalkBridge</p>
    </section>

    <section class="card card--back" aria-label="Business card back">
      <div class="contact">
        <h1 class="contact__title">TALKBRIDGE</h1>
        <span class="contact__dot"></span>
        <p class="contact__line">ElenaVT@talkbridge-demo.co.uk</p>
        <p class="contact__line">TalkBridge-demo.co.uk</p>
        <p class="contact__line">London, UK</p>
      </div>
    </section>
  </main>
</body>
</html>
```